Stationery Design for Consulting Company
Orvel Partners
Creative Brief
Professional
Tomas Wenholt
Director
Orvel Partners LLC 48215 Ridgefern Road Dunmore, DE 19872 USA
tomas@orvel-advisory.com
www.orvel-advisory.com
Maybe just a larger logo in the middle unless you have better ideas. I'm open to suggestions.

```html
<!DOCTYPE html>
<html lang="en">
<head>
<meta charset="utf-8">
<title>Orvel Partners – Business Card</title>
<link rel="stylesheet" href="https://fonts.googleapis.com/css2?family=Roboto:wght@400;500;700&display=swap">
<style>
  :root {
    --backdrop: #3b3b3d;
    --card: #ffffff;
    --accent: #f6a828;
    --ink: #2b2b2b;
    --ink-soft: #444444;
    --rule: #222222;
  }
  * { box-sizing: border-box; margin: 0; padding: 0; }
  html, body {
    width: 1200px; height: 816px; overflow: hidden;
    background: var(--backdrop);
    font-family: "Roboto", sans-serif;
  }
  .card {
    position: absolute; left: 100px; top: 118px;
    width: 1000px; height: 580px;
    background: var(--card);
    border-radius: 44px;
    overflow: hidden;
  }
  .card__art { position: absolute; inset: 0; }
  .brand {
    position: absolute; left: 62px; top: 150px;
    color: var(--accent);
    font-weight: 500; font-size: 40px; letter-spacing: 0.5px;
    display: flex; align-items: center; gap: 14px;
  }
  .brand__dot {
    width: 22px; height: 22px; border-radius: 50%;
    background: var(--accent);
  }
  .person {
    position: absolute; left: 150px; top: 256px;
    text-align: center; width: 250px;
    color: var(--ink);
  }
  .person__name { font-size: 32px; font-weight: 500; line-height: 1.1; }
  .person__role {
    font-size: 19px; font-weight: 700; letter-spacing: 1.2px;
    text-transform: uppercase; margin-top: 6px;
  }
  .address {
    position: absolute; right: 64px; top: 282px;
    display: flex; gap: 12px; align-items: flex-start;
    color: var(--ink-soft); font-size: 20px; line-height: 1.4;
    text-align: right;
  }
  .address svg { margin-top: 4px; }
  .contacts {
    position: absolute; left: 62px; bottom: 56px;
    list-style: none;
    color: var(--ink-soft); font-size: 20px;
  }
  .contacts li { display: flex; align-items: center; gap: 18px; height: 38px; }
  .contacts svg { width: 20px; height: 20px; flex: none; }
</style>
</head>
<body>
<main class="card">
  <svg class="card__art" width="1000" height="580" viewBox="0 0 1000 580" aria-hidden="true">
    <path d="M0 244 H378 A44 44 0 0 1 378 332 H0 Z" fill="var(--accent)"/>
    <path d="M370 244 C395 238 400 228 430 228 H1000" fill="none" stroke="var(--rule)" stroke-width="3"/>
  </svg>

  <div class="brand"><span class="brand__dot"></span>Orvel Partners LLC</div>

  <div class="person">
    <p class="person__name">Tomas Wenholt</p>
    <p class="person__role">Director</p>
  </div>

  <div class="address">
    <svg width="20" height="18" viewBox="0 0 20 18" aria-hidden="true">
      <path d="M10 1 L19 9 H16 V17 H12 V12 H8 V17 H4 V9 H1 Z" fill="var(--ink)"/>
    </svg>
    <p>48215 Ridgefern Road,<br>Dunmore, DE 19872, USA</p>
  </div>

  <ul class="contacts">
    <li>
      <svg viewBox="0 0 20 20" aria-hidden="true"><path d="M5 2 L8 6 L6.5 8 C7.5 10.5 9.5 12.5 12 13.5 L14 12 L18 15 L16 18 C9 18 2 11 2 4 Z" fill="var(--ink)"/></svg>
      +1 (302) 482-1590
    </li>
    <li>
      <svg viewBox="0 0 20 20" aria-hidden="true"><rect x="2" y="4" width="16" height="12" rx="1.5" fill="var(--ink)"/><path d="M3 5 L10 11 L17 5" fill="none" stroke="#fff" stroke-width="1.5"/></svg>
      tomas@orvel-advisory.com
    </li>
    <li>
      <svg viewBox="0 0 20 20" aria-hidden="true"><circle cx="10" cy="10" r="8" fill="none" stroke="var(--ink)" stroke-width="2"/><ellipse cx="10" cy="10" rx="3.5" ry="8" fill="none" stroke="var(--ink)" stroke-width="1.5"/><path d="M2 10 H18 M3.5 6 H16.5 M3.5 14 H16.5" stroke="var(--ink)" stroke-width="1.5"/></svg>
      www.orvel-advisory.com
    </li>
  </ul>
</main>
</body>
</html>
```